Corvane Project Services - Flyer

Project Breif:
I need a single page A4 Capability Statement, which will be used to market our services to prospective clients, both in print and via email PDF.
It needs to look professional and should incorporate the elements I have uploaded into files, these include:
Capability Statement Text
Corvane Services Company Logo
Additional Logo’s (Tools We Use)
Glimmer Bay Pics can be cut into the page
I have included examples of capability statements as a guide to what i am looking for.
Regards
Derek
Engineering Consulting

```html
<!DOCTYPE html>
<html lang="en">
<head>
<meta charset="utf-8">
<title>Corvane Project Services – Capability Statement</title>
<link rel="stylesheet" href="https://fonts.googleapis.com/css2?family=Roboto:wght@400;500;700&family=Roboto+Condensed:wght@400;700&display=swap">
<style>
  :root {
    --page-bg: #d4d4d4;
    --paper: #ffffff;
    --brand-blue: #0b57a4;
    --deep-blue: #2d5fa8;
    --heading-blue: #0d4f9a;
    --panel-light: #eaf2f9;
    --panel-mid: #cfe5f2;
    --text: #3c3c3c;
    --text-dark: #2b2b2b;
    --photo-a: #dfe9f1;
    --photo-b: #f6f8fa;
    --photo-c: #c9d7e3;
  }
  * { margin: 0; padding: 0; box-sizing: border-box; }
  html, body { width: 1041px; height: 1200px; overflow: hidden; background: var(--page-bg); }
  body { position: relative; font-family: "Roboto", Arial, sans-serif; color: var(--text); }

  .flyer {
    position: absolute; left: 110px; top: 20px;
    width: 821px; height: 1160px;
    background: var(--paper);
    overflow: hidden;
    box-shadow: 0 10px 24px rgba(0,0,0,0.25);
  }

  /* Header */
  .brand {
    position: absolute; left: 0; top: 0; width: 100%; height: 126px;
    display: flex; align-items: center; justify-content: center; gap: 18px;
  }
  .brand-mark { width: 72px; height: 72px; border-radius: 50%; background: var(--brand-blue); }
  .brand-name {
    font-family: "Roboto", Arial, sans-serif; font-weight: 500;
    color: var(--text-dark); font-size: 25px; letter-spacing: 2px; line-height: 1.15;
    text-transform: uppercase;
  }
  .brand-name span { display: block; font-size: 17px; letter-spacing: 10px; }

  .accent-stripe { position: absolute; left: 405px; top: 126px; width: 416px; height: 11px; }

  .hero-photo {
    position: absolute; left: 0; top: 137px; width: 821px; height: 322px;
    background: linear-gradient(120deg, var(--photo-c) 0%, var(--photo-b) 40%, var(--photo-a) 70%, var(--photo-c) 100%);
  }

  /* Left column */
  .about-column {
    position: absolute; left: 18px; top: 459px; width: 392px; height: 701px;
    background: var(--panel-light);
  }
  .block { position: absolute; left: 0; width: 392px; }
  .block h2 {
    font-family: "Roboto Condensed", Arial, sans-serif; font-weight: 700;
    color: var(--heading-blue); font-size: 17px; margin-bottom: 4px;
  }
  .block p { font-size: 15px; line-height: 19.8px; text-align: justify; }
  .about { top: 22px; padding: 0 20px 0 32px; }
  .team { top: 187px; height: 105px; background: var(--panel-mid); padding: 12px 26px 0 25px; }
  .team p { line-height: 20px; text-align: left; }
  .expertise { top: 315px; padding: 0 26px 0 25px; }
  .expertise h2 { margin-bottom: 8px; }
  .expertise p { line-height: 18px; margin-bottom: 18px; }

  /* Right column */
  .services-bar {
    position: absolute; left: 410px; top: 459px; width: 411px; height: 50px;
    background: var(--brand-blue); color: #fff;
    font-family: "Roboto Condensed", Arial, sans-serif; font-weight: 700; font-size: 19px;
    padding: 14px 0 0 63px;
  }
  .service { position: absolute; left: 423px; width: 390px; }
  .service-icon { position: absolute; left: 0; top: 0; width: 40px; height: 40px; }
  .service h3 {
    margin-left: 50px; padding-top: 7px;
    font-family: "Roboto Condensed", Arial, sans-serif; font-weight: 700;
    color: var(--heading-blue); font-size: 16.5px;
  }
  .service ul { list-style: none; margin: 5px 0 0 47px; }
  .service li {
    position: relative; padding-left: 19px;
    font-family: "Roboto Condensed", Arial, sans-serif; font-size: 15.5px; line-height: 20px; color: var(--text);
  }
  .service li::before {
    content: ""; position: absolute; left: 2px; top: 8px; width: 5px; height: 5px; background: var(--text);
  }
  .planning { top: 523px; }
  .risk { top: 702px; }
  .cost { top: 871px; }

  .contact-bar { position: absolute; left: 410px; top: 1022px; width: 52px; height: 138px; background: var(--deep-blue); }
  .contacts { position: absolute; left: 483px; top: 1026px; list-style: none; }
  .contacts li {
    display: flex; align-items: center; gap: 12px; height: 42px;
    font-family: "Roboto", Arial, sans-serif; font-weight: 500; font-size: 20px; color: var(--text-dark);
  }
  .contacts svg { width: 30px; height: 30px; flex: none; }
</style>
</head>
<body>
<main class="flyer">
  <header class="brand">
    <div class="brand-mark"></div>
    <div class="brand-name">Corvane Project <span>Services</span></div>
  </header>

  <svg class="accent-stripe" viewBox="0 0 416 11" preserveAspectRatio="none" aria-hidden="true">
    <polygon points="14,0 416,0 416,11 0,11" fill="#0b57a4"/>
  </svg>

  <div class="hero-photo" role="img" aria-label="Photo of colleagues reviewing project documents and charts at a desk"></div>

  <section class="about-column">
    <div class="block about">
      <h2>About Us:</h2>
      <p>Our goal is to make successful project delivery more achievable and repeatable. We are continually innovating, evolving and learning, utilizing the latest industry tools and techniques to deliver real value to our clients. We are passionate about empowering organisations to achieve their objectives, on time and on budget.</p>
    </div>
    <div class="block team">
      <h2>Our Team</h2>
      <p>We use highly experienced industry professionals who engage with our clients to deliver practical and innovative project control solutions.</p>
    </div>
    <div class="block expertise">
      <h2>Our Expertise</h2>
      <p>For over 20 years we have been helping our clients to successfully deliver capital projects within the pharmaceutical and biotechnology sectors.</p>
      <p>During this time, we have worked closely with multinational healthcare companies and leading A&amp;E firms, on a variety of business-critical projects.</p>
      <p>Our experience and knowledge of project control gives our client’s unparalleled visibility of Cost, Schedule and Risk through the lifecycle of their projects.</p>
      <p>This visibility allows our clients to make timely informed decisions which increase efficiency and project performance.</p>
    </div>
  </section>

  <div class="services-bar">Core Services:</div>

  <section class="service planning">
    <svg class="service-icon" viewBox="0 0 40 40" aria-hidden="true">
      <circle cx="20" cy="20" r="19" fill="#0b57a4"/>
      <rect x="11" y="12" width="16" height="15" fill="none" stroke="#fff" stroke-width="1.6"/>
      <line x1="11" y1="16" x2="27" y2="16" stroke="#fff" stroke-width="1.6"/>
      <line x1="15" y1="10" x2="15" y2="13" stroke="#fff" stroke-width="1.6"/>
      <line x1="23" y1="10" x2="23" y2="13" stroke="#fff" stroke-width="1.6"/>
      <circle cx="27" cy="26" r="4.5" fill="#0b57a4" stroke="#fff" stroke-width="1.4"/>
    </svg>
    <h3>Planning and Scheduling</h3>
    <ul>
      <li>Tender Planning</li>
      <li>Interactive Planning / Pull Planning</li>
      <li>CPM Planning &amp; Scheduling</li>
      <li>Agile / Lean Planning Methodology</li>
      <li>Independent Schedule Quality Assessment</li>
      <li>Schedule Risk Analysis (Monte Carlo)</li>
      <li>Training</li>
    </ul>
  </section>

  <section class="service risk">
    <svg class="service-icon" viewBox="0 0 40 40" aria-hidden="true">
      <circle cx="20" cy="20" r="19" fill="#0b57a4"/>
      <circle cx="14" cy="15" r="3.2" fill="#fff"/>
      <circle cx="26" cy="15" r="3.2" fill="#fff"/>
      <circle cx="20" cy="20" r="3.4" fill="#fff"/>
      <path d="M9 25 q5-6 10 0z M21 25 q5-6 10 0z M14 30 q6-7 12 0z" fill="#fff"/>
    </svg>
    <h3>Management of Risk</h3>
    <ul>
      <li>Risk Management Policies &amp; Procedures</li>
      <li>Risk Management Strategy</li>
      <li>Risk Registers</li>
      <li>Risk Response and Communication</li>
      <li>Cost &amp; Schedule Risk Analysis (Monte Carlo)</li>
      <li>Risk Management Training</li>
    </ul>
  </section>

  <section class="service cost">
    <svg class="service-icon" viewBox="0 0 40 40" aria-hidden="true">
      <circle cx="20" cy="20" r="19" fill="#0b57a4"/>
      <rect x="12" y="10" width="14" height="20" rx="1.5" fill="none" stroke="#fff" stroke-width="1.6"/>
      <rect x="14.5" y="12.5" width="9" height="4" fill="#fff"/>
      <g fill="#fff"><rect x="14.5" y="19" width="2.4" height="2.4"/><rect x="18" y="19" width="2.4" height="2.4"/><rect x="21.5" y="19" width="2.4" height="2.4"/><rect x="14.5" y="23" width="2.4" height="2.4"/><rect x="18" y="23" width="2.4" height="2.4"/><rect x="21.5" y="23" width="2.4" height="2.4"/></g>
      <circle cx="27" cy="27" r="4" fill="#0b57a4" stroke="#fff" stroke-width="1.4"/>
    </svg>
    <h3>Cost Control:</h3>
    <ul>
      <li>Estimating &amp; Forecasting</li>
      <li>Earned Value Management</li>
      <li>Progress Reporting</li>
      <li>Cost Risk Analysis (Monte Carlo)</li>
    </ul>
  </section>

  <div class="contact-bar"></div>
  <ul class="contacts">
    <li>
      <svg viewBox="0 0 30 30" aria-hidden="true"><circle cx="15" cy="15" r="14" fill="#0b57a4"/><path d="M11 8 l3 3 -2 2 q2 4 5 5 l2-2 3 3 -2 2 q-8-1-11-11z" fill="#fff"/></svg>
      +353 (0)865550142
    </li>
    <li>
      <svg viewBox="0 0 30 30" aria-hidden="true"><circle cx="15" cy="15" r="14" fill="#0b57a4"/><rect x="8" y="10" width="14" height="10" fill="none" stroke="#fff" stroke-width="1.6"/><path d="M8 10 l7 6 7-6" fill="none" stroke="#fff" stroke-width="1.6"/></svg>
      info@corvaneservices.ie
    </li>
    <li>
      <svg viewBox="0 0 30 30" aria-hidden="true"><circle cx="15" cy="15" r="14" fill="#0b57a4"/><circle cx="15" cy="15" r="8" fill="none" stroke="#fff" stroke-width="1.4"/><ellipse cx="15" cy="15" rx="3.5" ry="8" fill="none" stroke="#fff" stroke-width="1.4"/><line x1="7" y1="15" x2="23" y2="15" stroke="#fff" stroke-width="1.4"/></svg>
      www.corvaneservices.ie
    </li>
  </ul>
</main>
</body>
</html>
```